Medical group practice

We need a flyer design incorporating the three doctors in the practice, there is a general practitioner, ophthalmologist and an obstetrician & Gynaecologist. see the attached file for the concept. will leave the colour design up to you

Target Market(s)

general public

Industry/Entity Type

Health Care

Colors

Designer to choose colors to be used in the design.

Requirements
Must have
• logos included in attachement

```html
<!DOCTYPE html>
<html lang="en">
<head>
<meta charset="utf-8">
<title>Clearvale Medical – Flyer</title>
<link rel="stylesheet" href="https://fonts.googleapis.com/css2?family=Crimson+Text:wght@400;600;700&family=Arimo:wght@400;700&display=swap">
<style>
  :root {
    --sky-top: #e3eefa;
    --sky-mid: #f4f8fd;
    --white: #ffffff;
    --ink: #111111;
    --red: #d7262e;
    --red-dark: #a9161d;
    --purple: #6a1a7a;
    --green-name: #1f6b3a;
    --blue-name: #1e7ab8;
    --tick: #2a7fc1;
    --ob-red: #8c1a1a;
    --gyn-red: #c0202a;
    --meadow: #cfe39a;
    --strip: #dbe8f7;
    --serif: "Crimson Text", "Times New Roman", serif;
    --sans: "Arimo", Arial, sans-serif;
  }
  * { margin: 0; padding: 0; box-sizing: border-box; }
  html, body { width: 928px; height: 1200px; overflow: hidden; }
  body { background: var(--white); }
  .flyer {
    position: relative; width: 928px; height: 1200px; overflow: hidden;
    background: linear-gradient(180deg, var(--sky-top) 0%, var(--sky-mid) 30%, #ffffff 50%, #ffffff 100%);
    color: var(--ink);
  }
  .lower-field {
    position: absolute; left: 0; top: 595px; width: 928px; height: 587px;
    background: radial-gradient(ellipse 70% 60% at 95% 95%, var(--meadow) 0%, #e8f1cf 45%, rgba(255,255,255,0) 80%),
                linear-gradient(180deg, #eef5fc 0%, #ffffff 30%);
  }
  .bottom-strip { position: absolute; left: 0; top: 1182px; width: 928px; height: 18px; background: var(--strip); }

  .brand-mark { position: absolute; left: 52px; top: 70px; width: 170px; text-align: center; }
  .brand-mark .dot { width: 60px; height: 60px; border-radius: 50%; background: var(--red); margin: 0 auto 12px; }
  .brand-mark .word { font-family: var(--serif); font-weight: 700; font-size: 18px; color: var(--red); letter-spacing: 1px; }

  .masthead { position: absolute; left: 217px; top: 46px; width: 660px; text-align: center; }
  .masthead h1 {
    font-family: var(--serif); font-weight: 700; font-size: 54px; letter-spacing: 1px; line-height: 1;
    padding-bottom: 8px; border-bottom: 3px solid #333;
  }
  .masthead .tagline { font-family: var(--serif); font-size: 41px; line-height: 1; margin-top: 10px; }
  .masthead .contact { font-family: var(--serif); font-weight: 600; font-size: 14px; line-height: 18px; margin-top: 6px; }

  .ribbons { position: absolute; left: 0; top: 272px; }
  .ribbon { position: relative; height: 46px; }
  .ribbon svg { position: absolute; left: 0; top: 0; }
  .ribbon p {
    position: relative; padding-left: 35px; font-family: var(--serif); color: var(--white);
    font-size: 17px; line-height: 46px; white-space: nowrap;
  }
  .ribbon p b { font-weight: 600; font-size: 24px; }
  .ribbon.tall { height: 65px; }
  .ribbon.tall p { line-height: 26px; padding-top: 6px; }

  .hours { position: absolute; left: 34px; top: 460px; font-family: var(--serif); font-weight: 700; }
  .hours h2 { color: var(--red); font-size: 45px; line-height: 46px; }
  .hours p { font-size: 32px; line-height: 35px; }

  .photo { position: absolute; }
  .photo.family {
    left: 420px; top: 218px; width: 508px; height: 376px;
    background: radial-gradient(ellipse 80% 70% at 55% 55%, #e9e4df 0%, #d7d9dd 45%, rgba(240,244,250,0) 80%);
  }
  .photo.doctor {
    left: 0; top: 636px; width: 430px; height: 546px;
    background: radial-gradient(ellipse 70% 75% at 40% 60%, #f4f4f4 0%, #e6eaee 55%, rgba(255,255,255,0) 85%);
  }

  .profile { position: absolute; font-family: var(--sans); }
  .profile .practice-name { display: flex; align-items: center; gap: 8px; margin-bottom: 10px; }
  .profile .practice-name .dot { width: 34px; height: 34px; border-radius: 50%; }
  .profile .practice-name span { font-family: var(--sans); font-weight: 700; font-size: 17px; }
  .profile h3 { font-size: 20px; font-weight: 700; line-height: 24px; }
  .profile .role { font-size: 14px; font-weight: 700; line-height: 18px; }
  .profile .email { font-size: 14px; line-height: 18px; }
  .profile .email b { font-weight: 700; }
  .profile .services { font-size: 14px; line-height: 20px; margin-top: 8px; }

  .profile.eye { left: 302px; top: 648px; width: 300px; }
  .profile.eye .practice-name { margin-bottom: 16px; }
  .profile.eye .practice-name .dot { background: var(--purple); }
  .profile.eye .practice-name span { color: var(--purple); }
  .profile.eye h3 { color: var(--green-name); }

  .profile.gp { left: 617px; top: 648px; width: 300px; }
  .profile.gp .practice-name { margin-bottom: 16px; }
  .profile.gp .practice-name .dot { background: var(--blue-name); }
  .profile.gp .practice-name span { color: var(--blue-name); }
  .profile.gp h3 { color: var(--blue-name); }
  .checklist { list-style: none; margin-top: 6px; font-size: 14.5px; line-height: 20px; }
  .checklist li { display: flex; align-items: center; gap: 6px; }

  .profile.ob { left: 462px; top: 965px; width: 440px; }
  .profile.ob h3 { width: 300px; }
  .profile.ob .services span.obs { color: var(--ob-red); font-weight: 700; }
  .profile.ob .services span.gyn { color: var(--gyn-red); font-weight: 700; }
  .ob-mark { position: absolute; left: 750px; top: 995px; display: flex; align-items: center; gap: 8px; font-family: var(--sans); }
  .ob-mark .dot { width: 34px; height: 34px; border-radius: 50%; background: #1f5aa0; }
  .ob-mark span { font-weight: 700; font-size: 15px; color: #1f5aa0; width: 110px; line-height: 18px; }
</style>
</head>
<body>
<main class="flyer">
  <div class="lower-field"></div>
  <div class="bottom-strip"></div>

  <div class="brand-mark">
    <div class="dot"></div>
    <div class="word">CLEARVALE</div>
  </div>

  <header class="masthead">
    <h1>CLEARVALE MEDICAL</h1>
    <p class="tagline">Your Health is our Priority</p>
    <p class="contact">42 HARBOUR LANE, PORT WELLINGTON<br>TEL : (555) 310 2240 / 2241</p>
  </header>

  <div class="photo family" role="img" aria-label="Photo of a smiling multi-generation family in light clothing"></div>

  <section class="ribbons">
    <div class="ribbon">
      <svg width="490" height="46" viewBox="0 0 490 46"><polygon points="0,0 482,0 442,46 0,46" fill="var(--red)"/><polygon points="0,42 446,42 442,46 0,46" fill="var(--red-dark)"/></svg>
      <p>GENERAL PRACTITIONER - <b>(555) 480 1193</b></p>
    </div>
    <div class="ribbon">
      <svg width="470" height="46" viewBox="0 0 470 46"><polygon points="0,0 464,0 424,46 0,46" fill="var(--red)"/><polygon points="0,42 428,42 424,46 0,46" fill="var(--red-dark)"/></svg>
      <p>OPHTHALMOLOGIST - <b>(555) 482 7705</b></p>
    </div>
    <div class="ribbon tall">
      <svg width="450" height="65" viewBox="0 0 450 65"><polygon points="0,0 444,0 390,65 0,65" fill="var(--red)"/><polygon points="0,61 394,61 390,65 0,65" fill="var(--red-dark)"/></svg>
      <p>OBSTETRICIAN/GYNAECOLOGIST –<br><b>(555) 486 3320, (555) 219 4478</b></p>
    </div>
  </section>

  <section class="hours">
    <h2>OPENING HOURS</h2>
    <p>MONDAY – FRIDAYS 9AM-6PM,<br>SATURDAYS 10AM – 5PM</p>
  </section>

  <div class="photo doctor" role="img" aria-label="Photo of a smiling female doctor in a white coat with stethoscope and clipboard"></div>

  <section class="profile eye">
    <div class="practice-name"><div class="dot"></div><span>Brightview Eye Care</span></div>
    <h3>Dr. Lucia R. Fernandez</h3>
    <p class="role">MD. Surgeon Ophthalmologist</p>
    <p class="email"><b>Email:</b> lucia.eyes@example.com</p>
    <p class="services">Eyes disease examination,<br>Surgery of Pterygium, Cataract,<br>Glaucoma, Emergency: Conjunctivitis,<br>Traumatism, Foreign body and more<br>General Practitioner</p>
  </section>

  <section class="profile gp">
    <div class="practice-name"><div class="dot"></div><span>Holloway Practice</span></div>
    <h3>Dr. Marcus Holloway, MD.</h3>
    <p class="role">General Practitioner</p>
    <p class="email"><b>Email:</b> marcus.holloway.md@example.com</p>
    <ul class="checklist">
      <li><svg width="12" height="12" viewBox="0 0 12 12"><path d="M1 6.5 L4.5 10 L11 2" fill="none" stroke="var(--tick)" stroke-width="2.2"/></svg>General Checks</li>
      <li><svg width="12" height="12" viewBox="0 0 12 12"><path d="M1 6.5 L4.5 10 L11 2" fill="none" stroke="var(--tick)" stroke-width="2.2"/></svg>Annual Check ups</li>
      <li><svg width="12" height="12" viewBox="0 0 12 12"><path d="M1 6.5 L4.5 10 L11 2" fill="none" stroke="var(--tick)" stroke-width="2.2"/></svg>Wound Care/Dressings</li>
      <li><svg width="12" height="12" viewBox="0 0 12 12"><path d="M1 6.5 L4.5 10 L11 2" fill="none" stroke="var(--tick)" stroke-width="2.2"/></svg>Incision &amp; Drainage</li>
      <li><svg width="12" height="12" viewBox="0 0 12 12"><path d="M1 6.5 L4.5 10 L11 2" fill="none" stroke="var(--tick)" stroke-width="2.2"/></svg>Suturing lacerations</li>
      <li><svg width="12" height="12" viewBox="0 0 12 12"><path d="M1 6.5 L4.5 10 L11 2" fill="none" stroke="var(--tick)" stroke-width="2.2"/></svg>Pain Injections</li>
      <li><svg width="12" height="12" viewBox="0 0 12 12"><path d="M1 6.5 L4.5 10 L11 2" fill="none" stroke="var(--tick)" stroke-width="2.2"/></svg>Glucose checks</li>
      <li><svg width="12" height="12" viewBox="0 0 12 12"><path d="M1 6.5 L4.5 10 L11 2" fill="none" stroke="var(--tick)" stroke-width="2.2"/></svg>Foreign Body Removal</li>
    </ul>
  </section>

  <section class="profile ob">
    <h3>Dr. Anil Sethna, BMedSci, MBBS, DM (O&amp;G), FACOG</h3>
    <p class="role">Obstetrician &amp; Gynaecologist</p>
    <p class="email"><b>Email:</b> dr.sethna@example.com</p>
    <p class="services"><span class="obs">Obstetrics:</span>&nbsp;&nbsp; Prenatal Care, Delivery,<br>Postnatal checks, High Risk pregnancy<br><span class="gyn">Gynaecology:</span> Pap smears, Abnormal vaginal bleeding,<br>Fibroids, Colposcopy, Family planning, Infertility,<br>Cancer screening, And More....</p>
  </section>

  <div class="ob-mark"><div class="dot"></div><span>Sethna Women's Health</span></div>
</main>
</body>
</html>
```